Redesign cement bags for leading cement producer in south east asia

We are from Larkfield cement and would like to redesign our bag to relaunch the product line. Our bags are made of high quality PP woven sack. We are one of the leading cement producers and we want our bags to have a Larkfield classy look on each visible side when it is loading in a truck or stacking on a pallet.

Thank you for interesting in this project. Good luck.

Project Deadline Extended Reason: Hi all, I have received requests to extend the deadline. Some of the work requires revising and some of them are still on process. To be fair, I also raise my budget to compensate the time. Thanks all for your participation. Added Sunday, July 10, 2016

Target Market(s)

Construction

Industry/Entity Type

Cement

Requirements
Must have
• You will have to design two bags for two cement grades. 52.5 is of higher grade and 42.5 is of lower grade. Both are similar in design but a distinctive colours to differentiate the two at once. Please look at Reference picture 2 for ideas.
Nice to have
• You do not have to change the original logo but the Larkfield cement word font changes are required. There are no restrictions to colours and font but please refrain from using feminine colours. Instructions on rear side of the bags are now included in the scope. Please create new layout and design new user friendly symbols.
Should not have
• Since cement is a dusty product, you need avoid some colours like black as background. The dust need to be less obvious to attract attention. Our previous base colour are shown in below.
• We want a fresh look on our bag, please do not just copy our old design and make small changes. I have attached our competitors' design, please refrain from using their design as well.
• It is recommend to do some research on cement bag sector.

```html
<!DOCTYPE html>
<html lang="en">
<head>
<meta charset="utf-8">
<title>Larkfield Portland Cement – Bag Range</title>
<link href="https://fonts.googleapis.com/css2?family=Montserrat:wght@700;800;900&display=swap" rel="stylesheet">
<style>
  :root {
    --grade-high: #d5141b;
    --grade-std: #1d59a5;
    --bag-white: #f3f3f3;
    --bag-shade: #e2e2e2;
    --stage-top: #8f8f8f;
    --stage-bottom: #e6e6e6;
    --ink-light: #ffffff;
  }
  * { box-sizing: border-box; margin: 0; padding: 0; }
  html, body { width: 1200px; height: 1200px; overflow: hidden; }
  body {
    background: linear-gradient(180deg, var(--stage-top) 0%, #c4c4c4 45%, var(--stage-bottom) 100%);
    font-family: "Montserrat", sans-serif;
    position: relative;
  }
  .bag {
    position: absolute;
    top: 203px;
    width: 472px;
    height: 740px;
    background: linear-gradient(90deg, var(--bag-shade) 0%, var(--bag-white) 20%, var(--bag-white) 80%, var(--bag-shade) 100%);
    overflow: hidden;
    color: var(--accent);
  }
  .bag--high { left: 100px; --accent: var(--grade-high); }
  .bag--std { left: 626px; --accent: var(--grade-std); }

  .brand {
    position: absolute; top: 44px; left: 0; right: 0;
    text-align: center;
  }
  .brand__name {
    font-weight: 900; font-size: 54px; letter-spacing: -1px; line-height: 1;
    text-transform: uppercase;
  }
  .brand__origin {
    font-weight: 800; font-size: 14px; letter-spacing: 0; margin-top: 4px;
    text-transform: uppercase;
  }
  .brand-disc {
    position: absolute; left: 50%; top: 200px;
    width: 250px; height: 250px; margin-left: -125px;
    border-radius: 50%; background: var(--accent);
  }
  .grade-band {
    position: absolute; left: 0; right: 0; top: 478px; bottom: 0;
    background: var(--accent);
  }
  .product {
    position: absolute; top: 483px; left: 0; right: 0;
    text-align: center; color: var(--ink-light);
    text-transform: uppercase;
  }
  .product__tag { font-weight: 900; font-size: 20px; letter-spacing: 1px; }
  .product__name { font-weight: 900; font-size: 46px; line-height: 44px; letter-spacing: -0.5px; margin-top: 4px; }

  .weight-corner {
    position: absolute; left: -120px; top: 645px;
    width: 280px; height: 280px; border-radius: 50%;
    background: var(--bag-white);
  }
  .weight {
    position: absolute; left: 26px; top: 690px;
  }
  .weight__label { font-weight: 800; font-size: 7px; text-transform: uppercase; }
  .weight__value { font-weight: 900; font-size: 31px; line-height: 1; }

  .strength {
    position: absolute; left: 288px; top: 630px; color: var(--ink-light);
  }
  .strength__label { font-weight: 800; font-size: 10px; line-height: 11px; text-transform: uppercase; }
  .strength__value { font-weight: 900; font-size: 80px; line-height: 1; letter-spacing: -3px; margin-top: 2px; margin-left: -12px; }
  .strength__value small { font-size: 36px; letter-spacing: 0; }
</style>
</head>
<body>
  <section class="bag bag--high" aria-label="Larkfield Portland cement 52.5 bag">
    <header class="brand">
      <div class="brand__name">Larkfield</div>
      <div class="brand__origin">Product of Myanmar</div>
    </header>
    <div class="brand-disc"></div>
    <div class="grade-band"></div>
    <div class="product">
      <div class="product__tag">Export quality</div>
      <div class="product__name">Portland<br>Cement</div>
    </div>
    <div class="weight-corner"></div>
    <div class="weight">
      <div class="weight__label">Net weight</div>
      <div class="weight__value">50kg</div>
    </div>
    <div class="strength">
      <div class="strength__label">Strength class<br>EN 197-1 (2000)</div>
      <div class="strength__value">52<small>.5</small></div>
    </div>
  </section>

  <section class="bag bag--std" aria-label="Larkfield Portland cement 42.5 bag">
    <header class="brand">
      <div class="brand__name">Larkfield</div>
      <div class="brand__origin">Product of Myanmar</div>
    </header>
    <div class="brand-disc"></div>
    <div class="grade-band"></div>
    <div class="product">
      <div class="product__tag">Export quality</div>
      <div class="product__name">Portland<br>Cement</div>
    </div>
    <div class="weight-corner"></div>
    <div class="weight">
      <div class="weight__label">Net weight</div>
      <div class="weight__value">50kg</div>
    </div>
    <div class="strength">
      <div class="strength__label">Strength class<br>EN 197-1 (2000)</div>
      <div class="strength__value">42<small>.5</small></div>
    </div>
  </section>
</body>
</html>
```